Brand Identity - Web and social media vegan challenge

Hello! We started by ouselves and need some huge help! :D We have a logo, a pack for our product and we need to put this together with web and social media design (with some colours and letters we have already used, but we are totally open to changes and suggestions!) We are a female founded business of vegan meals in Brazil, called Verdalumas, the aminoacid that produces serotonin, the hormone of happines! Our purpose is to create a sense that vegan and fitness food can be tasty and an act of self-care, and that with good habits people can improve and nourish their bodies and minds :) Our business model is to deliver the meals("marmitas") frozen weekly/monthly so people can subscribe for our service and always have food :) So the design should communicate, carefulness, energy, appetite and incetivate people to comeback ;P There goes the logo, some material we have used on social media and colors we have chosen according to the color we have for our plates/food pics ;) Lettering used: gill sans, blackout (midnight/sunrise/2am) and nexa bold.

Industry/Entity Type

Food Service

Coding

Coded - Design and coding required

Number of Pages Required

2 page

Font styles to use
Sans Serif

Requirements
Must have
• Landing page, menu, form for orders.
Nice to have
• color palette attached

```html
<!DOCTYPE html>
<html lang="en">
<head>
<meta charset="utf-8">
<title>Verdalumas — Vegan Meals</title>
<link rel="stylesheet" href="https://fonts.googleapis.com/css2?family=Lato:wght@700;900&family=Mulish:wght@400;600;700&display=swap">
<style>
:root{
  --black:#000;
  --white:#fff;
  --ink:#1a1a1a;
  --body:#3a3a3a;
  --red:#c8200e;
  --deep-red:#3a0a02;
  --yellow:#f7f03a;
  --teal:#a9e6dd;
  --peach:#f6d6b8;
  --grey:#9a9a9a;
  --line:#d6d6d6;
}
*{box-sizing:border-box;margin:0;padding:0}
html,body{width:1200px;height:3358px;overflow:hidden}
body{position:relative;background:var(--white);font-family:"Mulish",Arial,sans-serif;color:var(--body)}
.abs{position:absolute}
h1,h2,h3{font-family:"Lato","Helvetica Neue",sans-serif;color:var(--ink)}
.btn{display:flex;align-items:center;justify-content:center;border-radius:30px;font-family:"Mulish",Arial,sans-serif;font-weight:700}
.btn-outline{border:2px solid var(--red);color:var(--red);background:var(--white);font-size:17px}
.btn-yellow{background:var(--yellow);color:var(--ink)}

/* header */
.site-header{left:0;top:0;width:1200px;height:125px;background:var(--black)}
.brand{left:76px;top:14px;width:140px;display:flex;flex-direction:column;align-items:center;gap:8px}
.brand-dot{width:44px;height:44px;border-radius:50%;background:var(--white)}
.brand-name{font-family:"Lato",sans-serif;font-weight:900;font-size:19px;color:var(--white);letter-spacing:.5px}
.auth{top:20px;height:36px;width:97px;font-size:12px}
.auth-login{left:922px;background:var(--teal);color:var(--ink)}
.auth-signup{left:1028px;background:var(--red);color:var(--white)}
.main-nav{left:441px;top:84px;width:686px;display:flex;justify-content:space-between;font-size:12px;color:var(--white);letter-spacing:.4px}
.main-nav .current{color:var(--yellow)}

/* hero */
.hero{left:0;top:125px;width:1200px;height:540px;background:radial-gradient(ellipse at 68% 45%,#e4e4e4 0%,#a9a9a9 45%,#6a6a6a 100%)}
.hero-title{left:76px;top:150px;font-size:52px;color:var(--white);letter-spacing:2px;font-weight:900}
.hero-text{left:76px;top:212px;width:445px;font-size:15.5px;line-height:28px;color:var(--white);font-weight:600}
.hero-cta{left:76px;top:318px;width:193px;height:45px;font-size:18px}
.hero-photo{left:540px;top:95px;width:590px;height:300px;border-radius:28px;transform:rotate(8deg);background:linear-gradient(135deg,#f2f0e6 0%,#d9d3c1 30%,#6d2a1c 50%,#4a1f3e 62%,#c45a2a 80%,#ece8da 100%);box-shadow:0 20px 40px rgba(0,0,0,.35)}

/* welcome */
.welcome-title{left:0;top:715px;width:1200px;text-align:center;font-size:32px}
.welcome-text{left:95px;top:772px;width:1010px;text-align:center;font-size:16px;line-height:33px}
.welcome-cta{left:510px;top:902px;width:180px;height:44px}

/* what we do */
.band-svg{left:0;width:1200px}
.what{left:0;top:1041px;width:1200px;height:379px;background:var(--peach)}
.what-photo{left:76px;top:54px;width:421px;height:271px;border-radius:10px;background:linear-gradient(120deg,#e8e8e8 0%,#f4f1e8 30%,#b87a4c 50%,#4a4a24 70%,#9a9a9a 100%)}
.what-title{left:524px;top:62px;font-size:32px}
.what-text{left:524px;top:122px;width:605px;font-size:15px;line-height:30px}
.what-cta{left:524px;top:264px;width:181px;height:45px}

/* how it works */
.how-title{left:0;top:1490px;width:1200px;text-align:center;font-size:32px}
.step{top:1560px;width:300px;display:flex;flex-direction:column;align-items:center;text-align:center}
.step svg{height:76px}
.step h3{margin-top:26px;font-family:"Mulish",sans-serif;font-weight:600;font-size:22px;color:var(--red)}
.step p{margin-top:6px;font-size:15px;line-height:24px}

/* plans */
.plans-bg{left:0;top:1827px;width:1200px;height:327px;background:linear-gradient(90deg,var(--peach) 0%,#efdcc4 45%,var(--teal) 100%)}
.plans-title{left:0;top:1866px;width:1200px;text-align:center;font-size:32px}
.plan{top:1976px;width:282px;height:388px;background:var(--white);border:1.5px solid var(--line);border-radius:12px;box-shadow:0 2px 6px rgba(0,0,0,.08)}
.plan-head{position:absolute;left:22px;top:-33px;width:238px;height:123px;border-radius:14px;background:linear-gradient(180deg,#0c0200 0%,var(--deep-red) 45%,#b32109 100%);transform:skewY(-4deg);display:flex;flex-direction:column;align-items:center;justify-content:center;color:var(--white);font-family:"Lato",sans-serif;font-weight:900;line-height:1}
.plan-head .name{font-size:26px}
.plan-head .price{font-size:38px;color:var(--yellow);margin-top:2px}
.plan-head .per{font-size:22px;margin-top:2px}
.plan ul{list-style:none;position:absolute;left:0;top:112px;width:100%;text-align:center;font-size:15px;line-height:34px}
.plan .btn{position:absolute;left:51px;top:330px;width:179px;height:37px;font-size:16px}

/* testimonial */
.voices{left:0;top:2429px;width:1200px;height:360px;background:linear-gradient(135deg,#f3cfae 0%,var(--peach) 50%,#f0d2b4 100%)}
.voices-title{left:0;top:58px;width:1200px;text-align:center;font-size:32px}
.avatar{left:164px;top:139px;width:134px;height:134px;border-radius:50%;border:4px solid var(--white);background:radial-gradient(circle at 50% 40%,#b07a55 0%,#6a3a22 70%,#3a1e12 100%)}
.quote{left:343px;top:140px;width:700px;font-size:14px;line-height:27px}
.quote-name{left:343px;top:256px;font-size:16px;color:var(--red);font-weight:600}
.arrow{top:191px}

/* newsletter */
.news-title{left:0;top:2862px;width:1200px;text-align:center;font-size:32px}
.news-sub{left:0;top:2920px;width:1200px;text-align:center;font-size:17px}
.news-form{left:253px;top:2971px;width:692px;height:47px;border:1.5px solid var(--line);border-radius:30px;display:flex;align-items:center;padding:0 6px 0 24px;font-size:14px;color:#555}
.news-form .btn{margin-left:auto;width:128px;height:35px;background:var(--teal);color:var(--ink);font-size:16px}

/* footer */
.site-footer{left:0;top:3135px;width:1200px;height:223px;background:var(--black)}
.footer-brand{left:0;top:3080px;width:1200px;display:flex;flex-direction:column;align-items:center;gap:10px}
.footer-brand .brand-dot{width:50px;height:50px;background:var(--ink);border:3px solid var(--white)}
.footer-brand .brand-name{font-size:22px}
.footer-nav{left:0;top:3225px;width:1200px;display:flex;justify-content:center;gap:41px;font-size:12px;color:var(--white);letter-spacing:.4px}
.copyright{left:0;top:3260px;width:1200px;text-align:center;font-size:11px;color:var(--grey)}
.social{left:0;top:3292px;width:1200px;display:flex;justify-content:center;gap:24px}
.social span{width:18px;height:18px;border-radius:50%;background:#cfcfcf}
</style>
</head>
<body>

<header class="abs site-header">
  <div class="abs brand"><span class="brand-dot"></span><span class="brand-name">VERDALUMAS</span></div>
  <a class="abs btn auth auth-login">LOG IN</a>
  <a class="abs btn auth auth-signup">SIGN UP</a>
  <nav class="abs main-nav"><span class="current">HOME</span><span>ABOUT US</span><span>SERVICES</span><span>HOW IT WORKS</span><span>PLANS</span><span>BLOG</span><span>CONTACT US</span></nav>
</header>

<section class="abs hero">
  <div class="abs hero-photo" role="img" aria-label="Vegan meal in a takeaway tray with beans, red cabbage, carrot and stew"></div>
  <h1 class="abs hero-title">VERDALUMAS</h1>
  <p class="abs hero-text">We are a female founded business of vegan meals in Brazil, called Verdalumas, the amino acid that produces serotonin, the hormone of happiness!</p>
  <a class="abs btn btn-yellow hero-cta">Get Started</a>
</section>

<h2 class="abs welcome-title">Welcome to Our Website</h2>
<p class="abs welcome-text">Lorem ipsum dolor sit amet, consectetur adipiscing elit. Vestibulum at risus vitae metus fringilla tristique. Nulla facilisi. Mauris interdum faucibus risus non lacinia. Sed vulputate neque eget metus porttitor, ac consectetur felis portao varius natoque penatibus et magnis dis parturient montes, nascetur ridiculus mus.</p>
<a class="abs btn btn-outline welcome-cta">Read More</a>

<svg class="abs band-svg" style="top:1007px" height="34" viewBox="0 0 1200 34" aria-hidden="true"><polygon points="0,0 600,34 0,34" fill="var(--red)"/></svg>

<section class="abs what">
  <div class="abs what-photo" role="img" aria-label="Meal tray with rice, grated carrot and lentil stew"></div>
  <h2 class="abs what-title">What We Do</h2>
  <p class="abs what-text">Lorem ipsum dolor sit amet, consectetur adipiscing elit. Vestibulum at risus vitae metus fringilla tristique. Nulla facilisi. Interdum faucibus risus non lacinia. Sed vulputate neque eget metus porttitor, ac consectetur felis portao varius natoque penatibus et magnis dis parturient montes, nascetur ridiculus mus.</p>
  <a class="abs btn btn-outline what-cta">Read More</a>
</section>

<svg class="abs band-svg" style="top:1420px" height="31" viewBox="0 0 1200 31" aria-hidden="true"><polygon points="600,0 1200,0 1200,31" fill="var(--red)"/></svg>

<h2 class="abs how-title">How It Works</h2>
<div class="abs step" style="left:90px">
  <svg viewBox="0 0 60 76" width="60" aria-hidden="true" fill="none" stroke="#111" stroke-width="2.5"><path d="M4 3h36l16 16v54H4z"/><path d="M40 3v16h16"/><rect x="18" y="30" width="26" height="7"/><rect x="18" y="41" width="26" height="7"/><rect x="18" y="52" width="26" height="7"/></svg>
  <h3>Suspendisse</h3>
  <p>Lorem ipsum dolor sit amet,<br>consectetur adipiscing elit at risus<br>vitae metus fringilla tristique.</p>
</div>
<div class="abs step" style="left:448px">
  <svg viewBox="0 0 68 76" width="68" aria-hidden="true" fill="none" stroke="#111" stroke-width="2.5"><rect x="3" y="12" width="62" height="60" rx="4"/><path d="M3 26h62M18 4v14M50 4v14M3 40h62M3 55h62M18 26v46M34 26v46M50 26v46"/></svg>
  <h3>Suspendisse</h3>
  <p>Lorem ipsum dolor sit amet,<br>consectetur adipiscing elit at risus<br>vitae metus fringilla tristique.</p>
</div>
<div class="abs step" style="left:810px">
  <svg viewBox="0 0 120 60" width="120" aria-hidden="true" fill="none" stroke="#111" stroke-width="2.5"><path d="M10 6h100l8 48H2z"/><rect x="14" y="14" width="40" height="32" rx="4"/><rect x="60" y="14" width="44" height="32" rx="4"/><path d="M22 20v20M30 20v20M38 20v20M46 20v20"/><circle cx="82" cy="30" r="9"/></svg>
  <h3>Suspendisse</h3>
  <p>Lorem ipsum dolor sit amet,<br>consectetur adipiscing elit at risus<br>vitae metus fringilla tristique.</p>
</div>

<div class="abs plans-bg"></div>
<h2 class="abs plans-title">Subscription Plans</h2>
<article class="abs plan" style="left:164px">
  <div class="plan-head"><span class="name">Basic</span><span class="price">$12.00</span><span class="per">pm</span></div>
  <ul><li>Lorem ipsum dolor</li><li>Sit amet</li><li>Consectetur adipiscing</li><li>Elit at risus vitae</li><li>Metus fringilla</li><li>Tristique</li></ul>
  <a class="btn btn-yellow">Subscribe Now</a>
</article>
<article class="abs plan" style="left:459px">
  <div class="plan-head"><span class="name">Standard</span><span class="price">$16.00</span><span class="per">pm</span></div>
  <ul><li>Lorem ipsum dolor</li><li>Sit amet</li><li>Consectetur adipiscing</li><li>Elit at risus vitae</li><li>Metus fringilla</li><li>Tristique</li></ul>
  <a class="btn btn-yellow">Subscribe Now</a>
</article>
<article class="abs plan" style="left:755px">
  <div class="plan-head"><span class="name">Premium</span><span class="price">$19.00</span><span class="per">pm</span></div>
  <ul><li>Lorem ipsum dolor</li><li>Sit amet</li><li>Consectetur adipiscing</li><li>Elit at risus vitae</li><li>Metus fringilla</li><li>Tristique</li></ul>
  <a class="btn btn-yellow">Subscribe Now</a>
</article>

<svg class="abs band-svg" style="top:2400px" height="29" viewBox="0 0 1200 29" aria-hidden="true"><polygon points="600,29 1200,0 1200,29" fill="var(--red)"/></svg>

<section class="abs voices">
  <h2 class="abs voices-title">What Our Member Says..</h2>
  <svg class="abs arrow" style="left:98px" width="16" height="30" viewBox="0 0 16 30" aria-hidden="true"><path d="M14 2L3 15l11 13" fill="none" stroke="#333" stroke-width="2.5"/></svg>
  <div class="abs avatar" role="img" aria-label="Portrait photo of a smiling member"></div>
  <p class="abs quote">" Excepteur sint occaecat cupidatat non proident, sunt in culpa qui officia deserunt mollit anim id est laborum. Sed ut perspiciatis unde omnis iste natus error sit voluptatem accusantium laudantium, totam rem aperiam, eaque ipsa quae ab illo inventore veritatis et quasi. Sed ut perspiciatis unde omnis iste natus error sit voluptatem accusantium laudantium, totam rem aperiam... "</p>
  <p class="abs quote-name">-Name Heading</p>
  <svg class="abs arrow" style="left:1088px" width="16" height="30" viewBox="0 0 16 30" aria-hidden="true"><path d="M2 2l11 13L2 28" fill="none" stroke="#333" stroke-width="2.5"/></svg>
</section>

<svg class="abs band-svg" style="top:2789px" height="28" viewBox="0 0 1200 28" aria-hidden="true"><polygon points="0,0 600,0 0,28" fill="var(--red)"/></svg>

<h2 class="abs news-title">Join Email Listing</h2>
<p class="abs news-sub">Lorem ipsum dolor sit amet, consectetur adipiscing elit.</p>
<form class="abs news-form"><span>Enter Email Address</span><a class="btn">Subscribe</a></form>

<footer class="abs site-footer"></footer>
<div class="abs footer-brand"><span class="brand-dot"></span><span class="brand-name">VERDALUMAS</span></div>
<nav class="abs footer-nav"><span>HOME</span><span>ABOUT US</span><span>SERVICES</span><span>HOW IT WORKS</span><span>PLANS</span><span>BLOG</span><span>CONTACT US</span></nav>
<p class="abs copyright">Copyright © 2019 Company Name.  All Rights Reserved.</p>
<div class="abs social" aria-label="Social links"><span></span><span></span><span></span><span></span></div>

</body>
</html>
```